Professional Services (B-2-B) Business Cards (Front & Back)

Quintarion is a business-to-business professional services company in the legal sector. They typically present to c-suite and executive functions who are looking for providers with expertise, and experience. Our business card should look and feel professional and contemporary, but we are not a startup tech company, so we want the tone to be more mature.

```html
<!DOCTYPE html>
<html lang="en">
<head>
<meta charset="UTF-8">
<title>Quintarion Business Cards</title>
<link href="https://fonts.googleapis.com/css2?family=Montserrat:wght@300;400;500;600&display=swap" rel="stylesheet">
<style>
  :root {
    --navy: #22407a;
    --silver: #c9ced6;
    --paper: #fafafa;
    --ink-grey: #8a8a8a;
    --backdrop: #e6e6e6;
    --white: #ffffff;
    --soft-white: #dfe4ee;
  }
  * { margin: 0; padding: 0; box-sizing: border-box; }
  html, body {
    width: 1200px; height: 801px; overflow: hidden;
    background: var(--backdrop);
    font-family: "Montserrat", sans-serif;
  }
  .sheet { position: relative; width: 1200px; height: 801px; }
  .card {
    position: absolute; top: 246px;
    width: 540px; height: 309px;
    overflow: hidden;
    box-shadow: 0 6px 18px rgba(0,0,0,0.15);
  }
  .card--front { left: 40px; background: var(--paper); }
  .card--back { left: 620px; background: var(--navy); }

  .wave { position: absolute; inset: 0; width: 540px; height: 309px; }

  .brand {
    position: absolute; display: flex; align-items: center; gap: 14px;
    font-weight: 500; letter-spacing: 0.25em; text-transform: uppercase;
    white-space: nowrap; line-height: 1;
  }
  .brand__mark { width: 15px; height: 15px; flex: none; }
  .card--front .brand { left: 38px; top: 72px; font-size: 24px; color: var(--ink-grey); }
  .card--front .brand__mark { background: var(--navy); }
  .card--back .brand { left: 50%; top: 50%; transform: translate(-50%, -50%); font-size: 30px; color: var(--white); }
  .card--back .brand__mark { background: var(--white); }

  .holder { position: absolute; left: 32px; bottom: 26px; color: var(--white); }
  .holder__name { font-weight: 600; font-size: 15px; letter-spacing: 0.03em; text-transform: uppercase; }
  .holder__title { font-weight: 300; font-size: 13px; margin-top: 3px; color: var(--soft-white); }

  .contact {
    position: absolute; right: 22px; top: 176px;
    list-style: none; color: var(--white);
    font-weight: 300; font-size: 12px; line-height: 20px;
  }
  .contact__item { display: flex; align-items: center; justify-content: flex-end; gap: 9px; }
  .contact__icon { width: 13px; height: 13px; flex: none; }
</style>
</head>
<body>
<main class="sheet">

  <section class="card card--front" aria-label="Card front">
    <svg class="wave" viewBox="0 0 540 309" aria-hidden="true">
      <path d="M0,168 C180,168 300,150 380,95 S470,30 540,24" fill="none" stroke="var(--silver)" stroke-width="10"/>
      <path d="M0,182 C180,182 300,164 384,109 S474,44 540,38" fill="none" stroke="var(--navy)" stroke-width="5"/>
      <path d="M0,194 C180,194 300,176 388,121 S478,56 540,50" fill="none" stroke="var(--navy)" stroke-width="5"/>
      <path d="M0,208 C180,208 300,190 392,135 S480,70 540,64 L540,309 L0,309 Z" fill="var(--silver)"/>
      <path d="M0,218 C180,218 300,200 396,145 S484,80 540,74 L540,309 L0,309 Z" fill="var(--navy)"/>
    </svg>

    <div class="brand"><span class="brand__mark"></span>Quintarion</div>

    <div class="holder">
      <p class="holder__name">Mark Ellison</p>
      <p class="holder__title">President &amp; CEO</p>
    </div>

    <ul class="contact">
      <li class="contact__item">(415) 555 - 0142
        <svg class="contact__icon" viewBox="0 0 14 14" aria-hidden="true"><circle cx="7" cy="7" r="6.3" fill="none" stroke="#fff"/><path d="M4.5,4 h1.5 l0.6,1.8 -0.9,0.7 a4,4 0 0 0 1.8,1.8 l0.7,-0.9 1.8,0.6 v1.5 a5.5,5.5 0 0 1 -5.5,-5.5z" fill="#fff"/></svg></li>
      <li class="contact__item">(203) 555 - 0187
        <svg class="contact__icon" viewBox="0 0 14 14" aria-hidden="true"><circle cx="7" cy="7" r="6.3" fill="none" stroke="#fff"/><rect x="5" y="3.5" width="4" height="7" rx="0.8" fill="#fff"/></svg></li>
      <li class="contact__item">mellison@quintarion.tech
        <svg class="contact__icon" viewBox="0 0 14 14" aria-hidden="true"><circle cx="7" cy="7" r="6.3" fill="none" stroke="#fff"/><rect x="4" y="4.8" width="6" height="4.4" fill="none" stroke="#fff" stroke-width="0.9"/><path d="M4,4.8 l3,2.4 3,-2.4" fill="none" stroke="#fff" stroke-width="0.9"/></svg></li>
      <li class="contact__item">www.quintarion.tech
        <svg class="contact__icon" viewBox="0 0 14 14" aria-hidden="true"><circle cx="7" cy="7" r="6.3" fill="none" stroke="#fff"/><circle cx="7" cy="7" r="3.4" fill="none" stroke="#fff" stroke-width="0.9"/><path d="M3.6,7 h6.8 M7,3.6 v6.8" stroke="#fff" stroke-width="0.9"/></svg></li>
    </ul>
  </section>

  <section class="card card--back" aria-label="Card back">
    <div class="brand"><span class="brand__mark"></span>Quintarion</div>
  </section>

</main>
</body>
</html>
```